LK Machining - flyer

We are a machine shop. While making sales calls in the field, we need a flyer to leave behind with prospect to attract interest.

Target Market(s)

Medical device, aerospace and aviation component manfacturers

Font styles to use
Serif

Colors

Designer to choose colors to be used in the design.

Requirements
Must have
• NA
Nice to have
• NA
Should not have
• NA

```html
<!DOCTYPE html>
<html lang="en">
<head>
<meta charset="utf-8">
<title>LK Machining – Flyer</title>
<link href="https://fonts.googleapis.com/css2?family=Montserrat:wght@300;400;600;700&family=Open+Sans:wght@300;400;600;700&family=Roboto:wght@400&display=swap" rel="stylesheet">
<style>
  :root{
    --red:#e8232a;
    --dark:#2b2726;
    --charcoal:#3a3b3d;
    --white:#ffffff;
    --paper:#f5f5f5;
    --ink:#3b3b3b;
    --muted:#6d6d6d;
    --canvas:#dcdcdc;
  }
  *{margin:0;padding:0;box-sizing:border-box}
  html,body{width:1200px;height:1200px;overflow:hidden;background:var(--canvas)}
  .flyer{
    position:absolute;left:191px;top:20px;width:854px;height:1210px;
    transform:scale(0.9587);transform-origin:0 0;
    background:var(--white);overflow:hidden;
    font-family:"Open Sans",sans-serif;color:var(--ink);
    box-shadow:0 2px 8px rgba(0,0,0,.25);
  }
  .flyer-shapes{position:absolute;left:0;top:0;width:854px;height:1210px}
  .brand{position:absolute;left:48px;top:108px;display:flex;align-items:center;gap:14px}
  .brand-name{font-family:"Montserrat",sans-serif;font-weight:600;font-size:38px;color:var(--dark);letter-spacing:-.5px}
  .brand-dot{width:34px;height:34px;border-radius:50%;background:var(--red)}
  .headline{position:absolute;right:36px;top:72px;text-align:right;font-family:"Montserrat",sans-serif;color:var(--white);line-height:1.12}
  .headline .line{display:block;font-weight:300;font-size:53px}
  .headline .accent{display:block;font-weight:700;font-size:53px;color:var(--red)}
  .headline-rule{position:absolute;right:36px;top:259px;width:84px;height:4px;background:var(--red)}
  .intro{position:absolute;right:32px;top:270px;width:320px;text-align:right;font-family:"Montserrat",sans-serif;font-weight:300;font-size:15.5px;line-height:1.27;color:var(--white);white-space:nowrap}
  .capabilities{position:absolute;left:60px;top:632px}
  .capabilities .kicker{display:block;font-family:"Montserrat",sans-serif;font-weight:300;font-size:33px;color:var(--ink);line-height:1.15}
  .capabilities .title{display:block;font-family:"Montserrat",sans-serif;font-weight:600;font-size:33px;color:var(--red);line-height:1.15}
  .capabilities .rule{width:60px;height:4px;background:var(--dark);margin-top:4px}
  .capabilities .lede{margin-top:12px;width:410px;font-family:"Montserrat",sans-serif;font-weight:300;font-size:20px;line-height:1.3;color:var(--muted)}
  .cap-list{position:absolute;left:60px;top:800px;list-style:none}
  .cap-list li{display:flex;align-items:center;height:41.5px;font-family:"Montserrat",sans-serif;font-size:21.5px;color:var(--ink)}
  .cap-list li::before{content:"";width:12px;height:12px;border-radius:50%;background:var(--red);margin:0 30px 0 6px}
  .hex-text{position:absolute;width:210px;text-align:center;font-family:"Open Sans",sans-serif;font-size:14.5px;line-height:1.35;color:var(--white)}
  .hex-text .hl{color:var(--red);font-weight:600;font-size:16px}
  .hex-text .hl-dark{color:var(--charcoal)}
  .hex-measure{left:510px;top:710px}
  .hex-clean{left:400px;top:910px}
  .hex-temp{left:622px;top:910px}
  .sectors{position:absolute;left:60px;top:1063px;font-family:"Open Sans",sans-serif;font-size:22.5px;color:var(--red)}
  .certs{position:absolute;left:60px;top:1092px;font-family:"Open Sans",sans-serif;font-weight:700;font-size:27px;color:var(--dark)}
  .footer{position:absolute;left:0;top:1133px;width:854px;height:77px;background:var(--charcoal);color:var(--white);font-family:"Roboto",sans-serif}
  .footer-stripe{position:absolute;left:0;top:0;width:697px;height:7px;background:var(--red)}
  .footer-address{position:absolute;left:110px;top:20px;font-size:18px;line-height:1.3}
  .footer-contact{position:absolute;left:538px;top:17px;font-size:15.5px;line-height:1.9}
  .footer svg{position:absolute}
</style>
</head>
<body>
<div class="flyer">
  <svg class="flyer-shapes" viewBox="0 0 854 1210">
    <defs>
      <linearGradient id="shopGlow" x1="0" y1="0" x2="1" y2="1">
        <stop offset="0" stop-color="#1f1b1a"/>
        <stop offset=".55" stop-color="#3a2c26"/>
        <stop offset="1" stop-color="#231d1b"/>
      </linearGradient>
      <radialGradient id="partsBlue" cx=".3" cy=".25" r=".35">
        <stop offset="0" stop-color="#b9cdf0"/>
        <stop offset="1" stop-color="#ffffff" stop-opacity="0"/>
      </radialGradient>
      <radialGradient id="partsGreen" cx=".6" cy=".55" r=".4">
        <stop offset="0" stop-color="#cfe6b4"/>
        <stop offset="1" stop-color="#ffffff" stop-opacity="0"/>
      </radialGradient>
      <radialGradient id="partsPurple" cx=".15" cy=".5" r=".3">
        <stop offset="0" stop-color="#e2c3e6"/>
        <stop offset="1" stop-color="#ffffff" stop-opacity="0"/>
      </radialGradient>
    </defs>
    <polygon points="320,0 854,0 854,820 527,600 0,600 0,262" fill="url(#shopGlow)" role="img" aria-label="Dim machine shop workspace photograph"/>
    <polygon points="0,0 320,0 410,135 340,262 0,262" fill="var(--paper)"/>
    <polygon points="0,596 520,596 854,815 854,830 515,607 0,607" fill="var(--red)"/>
    <polygon points="0,262 470,262 567,432 470,600 0,600" fill="var(--red)"/>
    <g role="img" aria-label="Product photo of titanium spinal screws with anodized blue, purple and green heads">
      <polygon points="0,272 462,272 553,432 462,592 0,592" fill="#f4f5f6"/>
      <polygon points="0,272 462,272 553,432 462,592 0,592" fill="url(#partsPurple)"/>
      <polygon points="0,272 462,272 553,432 462,592 0,592" fill="url(#partsBlue)"/>
      <polygon points="0,272 462,272 553,432 462,592 0,592" fill="url(#partsGreen)"/>
    </g>
    <polygon points="615,584 726,648 726,776 615,840 504,776 504,648" fill="var(--red)"/>
    <polygon points="505,782 613,845 613,970 505,1033 397,970 397,845" fill="var(--charcoal)" stroke="var(--red)" stroke-width="4"/>
    <polygon points="727,782 835,845 835,970 727,1033 619,970 619,845" fill="var(--charcoal)" stroke="var(--red)" stroke-width="4"/>
    <g fill="var(--white)">
      <rect x="563" y="657" width="112" height="8" rx="3"/>
      <rect x="562" y="648" width="8" height="46"/>
      <rect x="578" y="648" width="8" height="40"/>
      <rect x="592" y="654" width="20" height="16"/>
      <rect x="600" y="668" width="6" height="22"/>
    </g>
    <rect x="595" y="656" width="12" height="6" fill="var(--red)"/>
    <g fill="var(--white)">
      <rect x="484" y="853" width="30" height="40" rx="8" transform="rotate(-35 499 873)"/>
      <path d="M520 845 l10 -4 M522 852 l12 0" stroke="var(--white)" stroke-width="2"/>
      <circle cx="481" cy="893" r="3"/>
      <circle cx="515" cy="837" r="2.5"/>
    </g>
    <g fill="none" stroke="var(--white)" stroke-width="3">
      <path d="M722 878 v-40 a6 6 0 0 1 12 0 v40"/>
      <circle cx="728" cy="888" r="11"/>
      <path d="M740 846 h14 M718 868 h-14"/>
    </g>
    <circle cx="728" cy="888" r="6" fill="var(--white)"/>
    <text x="743" y="842" fill="var(--white)" font-family="Open Sans, sans-serif" font-size="13" font-weight="700">C+</text>
    <text x="697" y="868" fill="var(--white)" font-family="Open Sans, sans-serif" font-size="13" font-weight="700">C-</text>
  </svg>

  <div class="brand">
    <span class="brand-name">LK Machining</span>
    <span class="brand-dot"></span>
  </div>

  <h1 class="headline">
    <span class="line">Titanium</span>
    <span class="line">Spinal Screw</span>
    <span class="accent">Assemblies</span>
  </h1>
  <div class="headline-rule"></div>
  <p class="intro">Our Education, Training, and 25 years<br>of Medical and Aerospace machining<br>experience helps us determine the<br>best possible methods of manufacture<br>that will be most cost effective<br>for your parts.</p>

  <section class="capabilities">
    <span class="kicker">OUR</span>
    <span class="title">CAPABILITIES</span>
    <div class="rule"></div>
    <p class="lede">We make the parts, process them, and assemble them.</p>
  </section>
  <ul class="cap-list">
    <li>5 axis cnc milling</li>
    <li>Turning</li>
    <li>Cnc swiss-type</li>
    <li>Deburring</li>
    <li>Kvx visionscope 302</li>
    <li>Laser marking</li>
  </ul>

  <p class="hex-text hex-measure">Coordinate <span class="hl-dark">Measuring</span><br>machines, comparators,<br>sur-face plated<br>micrometers</p>
  <p class="hex-text hex-clean">Ultrasonic<br><span class="hl">Cleaning &amp; Reverse</span><br>osmosis water</p>
  <p class="hex-text hex-temp">Dedicated<br><span class="hl">Temperature Controlled</span><br>room</p>

  <p class="sectors">Medical, Implants, Aerospace, Aviation &amp; Military applications</p>
  <p class="certs">ISO 13485, 9100, 9001 CERTIFIED</p>

  <footer class="footer">
    <div class="footer-stripe"></div>
    <svg style="left:61px;top:26px" width="24" height="26" viewBox="0 0 24 26" aria-hidden="true">
      <path d="M12 2a9 9 0 0 1 9 9c0 6-9 13-9 13S3 17 3 11a9 9 0 0 1 9-9z" fill="none" stroke="var(--red)" stroke-width="2.5"/>
      <circle cx="12" cy="11" r="3" fill="var(--red)"/>
    </svg>
    <p class="footer-address">4120 Birch Street, Unit B,<br>Maple Valley, CA 90210</p>
    <svg style="left:500px;top:19px" width="22" height="22" viewBox="0 0 22 22" aria-hidden="true">
      <circle cx="11" cy="11" r="9" fill="none" stroke="var(--red)" stroke-width="2"/>
      <circle cx="11" cy="11" r="4.5" fill="var(--red)"/>
    </svg>
    <svg style="left:500px;top:48px" width="22" height="22" viewBox="0 0 22 22" aria-hidden="true">
      <circle cx="11" cy="11" r="9" fill="none" stroke="var(--red)" stroke-width="2"/>
      <path d="M7.5 6.5c.8-.8 1.6-.4 2 .4l.6 1.4c.2.6-.2 1-.6 1.3.5 1.2 1.4 2.1 2.6 2.6.3-.4.7-.8 1.3-.6l1.4.6c.8.4 1.2 1.2.4 2-1 1-3 1-5.4-1.4S6.5 7.5 7.5 6.5z" fill="var(--red)"/>
    </svg>
    <p class="footer-contact">www.lkmachiningworks.com<br>(555) 014-2870</p>
  </footer>
</div>
</body>
</html>
```